Professional Lawn Treatment flyer (double sided) needed for established gardening company

We are an established and trusted gardening company in Swindon, UK, and are about to launch a new Lawn Treatment Service. This will be marketed to both existing and new customers and needs to reflect our current professional image. The flyer will need to be double-sided, portrait orientation and correctly sized so to be printed on A5.

If you look on our website www.pelhamgardening.co.uk, you will see our colours are purple and green. We would like you to use these exact shades of purple and green in your design.

As part of the design, we will need you to put together an infographic table to show our packages. I have attached a spreadsheet which explains these packages but I will need you to create a visually appealing table that fits in with the overall design of the flyer. I don't want you to simply cut and paste my basic table into the design.

In terms of what needs to be included, I have tried to be as specific as possible here but please feel free to message me if you need any further information or clarification.

FRONT SIDE:
The title of our service is:
Expert Lawn Treatment Service

Our strapline will need to be included somewhere:
"Lawn care by your local gardening expert"

The front side of the flyer will need to contain our logo - different versions of which can be found within my dropbox folder here...

https://www.filecrate.net/sh/k7bq24nwxe9/QWT8PmRzLxKd3VuYcH0BnJeFa?dl=0

The front side will need to contain a main image (although feel free to add more if you have anything suitable). I have included a picture in the dropbox folder titled "Front side image" which we would like used. I've also included in the folder an adobe image of grass which you may or may not like to use on either front or back.

Somewhere on both the front and back sides, you will need to include our contact details:
01632 960481
www.pelhamgardening.co.uk/lawncare

The front side should show what treatments we currently have available. These are:

- Lawn Fertilising
- Scarification
- Aeration
- Weed Control
- Moss Control
- Hydration Booster
- Kempix
- Turfing & Renovation

"Select a one-off treatment or choose from one of our specially created lawn care packages."

BACK SIDE:
On the back, we will still need our logo and contact details but the image we'd like used should be the one in the dropbox folder titled "Back side image". Again, if you have any other images you feel would also work, then please feel free to add them.

The back side is to contain a bit more information and be a bit 'wordier' and so can you please include the following 2 paragraphs:

"As expert gardeners, we are passionate about horticulture and working to bring out the very best in your garden. When we work in your garden, we look at it and treat it with the same care and attention as if it were our own, before handing it back for you to enjoy. Our passion doesn't end at just trees and shrubs though. Your grass is as much of a living, breathing plant as your shrubs and we therefore utilise our expert horticultural knowledge to ensure your lawn thrives and reaches its fullest potential.

Lawn care isn't just about applying a fertiliser. It's about really understanding your lawn and being able to use extensive knowledge and experience to diagnose and treat issues. It therefore stands to reason that you should employ an expert to bring out the best in your lawn which is why we at Pelham Gardening Services have created a superior lawn care service that will keep your lawn looking lush, green and healthy all year round."

I referred at the very top of this brief to the fact we will need an infographic table created to show the different lawn care packages available. You see from the PDF table I created that we have 3 packages; Standard, Enhanced and Premium. Please create a visually appealing table which sets out the differences between our packages and include it on the back page.

Finally, somewhere we would like reference to the other gardening services we do. It's only to be something small as it isn't the main focus of the flyer but we think it would be good to mention what else we do. To re-iterate, it isnt to be big. I still want the main focus to be lawn care but if you could somehow reference that we also do the following services, that would be good. I will leave it to you to decide where on the flyer it fits in best, be it the front or back:

- Lawn mowing
- Shrub pruning
- Hedge trimming
- Weed killing
- Garden clearance & tidy-up
- Planting & design
- Regular Garden Maintenance
- Turfing
- Fencing
- Gutter clearance

I think thats it. I look forward to your designs!
Ps. Don't forget the dropbox folder:

Target Market(s)

Professional men/women aged 25+
Retired aged 65+

Industry/Entity Type

Home And Garden

Font styles to use
Sans Serif

Colors
6b449b
9bcb3c

Requirements
Must have
• Our company colours; purple and green; as per our website www.pelhamgardening.co.uk. I've selected purple and green on this brief just to highlight the colours needed but please be sure to use the exact shades from our website and NOT the shade of purple and green that were selected on this brief.
• All the wording as explained in the main project brief.
Nice to have
• I want the flyer to be bold, eye-catching and modern.
• We particularly like the font Trebuchet MS for general copy but please feel free to use any other font for bolder, main titles.
Should not have
• We don't want anything gimmicky. No cheesy marketing.
• We only want professional looking designs. With the greatest of respect, if you're just starting out or don't really do design but think you'll use this as practise, please don't waste your or our time. We've previously run contests for other projects where we've had designs submitted that have clearly been done on MS Word and used Clipart and Wordart. That's really not what we are looking for.

```html
<!DOCTYPE html>
<html lang="en">
<head>
<meta charset="utf-8">
<title>Pelham Gardening Services – Expert Lawn Treatment Service</title>
<link href="https://fonts.googleapis.com/css2?family=Ubuntu:wght@400;500;700&display=swap" rel="stylesheet">
<style>
:root{
  --green:#2f9a3c;
  --green-dark:#1f7a30;
  --green-light:#6cc04a;
  --purple:#7a2a82;
  --purple-dark:#5e1f66;
  --yellow:#f6e71d;
  --olive:#8fa22c;
  --text:#222;
  --grey:#555;
  --bg:#ebe7e0;
  --cell-std:#f5f6dc;
  --cell-enh:#e1f0e0;
  --cell-pre:#f8e9f3;
  --row-a:#f1f1f1;
  --tick:#3aa53d;
  --cross:#e0262b;
}
*{box-sizing:border-box;margin:0;padding:0}
html,body{width:1200px;height:960px;overflow:hidden;background:var(--bg);font-family:"Ubuntu",sans-serif;color:var(--text)}
.page{position:absolute;top:110px;width:530px;height:758px;background:#fff;overflow:hidden;box-shadow:0 4px 14px rgba(0,0,0,.25)}
.page--front{left:56px}
.page--back{left:629px}
.page-art{position:absolute;inset:0}
.abs{position:absolute}

/* front */
.brand{left:28px;top:96px;width:250px;display:flex;align-items:center;gap:10px}
.brand-mark{width:22px;height:22px;border-radius:50%;background:var(--green);flex:none}
.brand-name{font-size:22px;font-weight:700;color:var(--purple);line-height:1.1}
.strapline{left:292px;top:32px;width:230px;color:#fff;font-size:21px;font-weight:500;line-height:1.2;text-shadow:0 1px 3px rgba(0,0,0,.35)}
.title-band{left:242px;top:276px;width:288px;height:92px;background:rgba(31,122,48,.72)}
.service-title{left:250px;top:283px;color:#fff;font-size:32px;font-weight:500;line-height:1.16}
.treatments{left:32px;top:463px;list-style:none}
.treatments li{font-size:14px;font-weight:500;height:24.4px;display:flex;align-items:center;gap:10px}
.treatments li::before{content:"";width:11px;height:8px;background:var(--green-light);border-radius:0 8px 0 8px;flex:none}
.select-note{left:34px;top:668px;width:240px;font-size:13px;line-height:1.18}
.contact{background:var(--purple);color:#fff;text-align:center}
.contact--front{left:291px;top:582px;width:219px;height:123px;border-radius:0 0 14px 14px;padding-top:24px}
.contact-lead{font-size:13px}
.contact-phone{font-size:28px;font-weight:500;letter-spacing:.5px;margin:4px 0 1px}
.contact-url{font-size:12px;font-weight:500}
.grass-strip{left:0;bottom:0;width:530px;height:36px;background:linear-gradient(#9fd36a,#3d9a2e)}

/* back */
.intro{left:29px;top:13px;width:480px;color:#fff;font-size:12.6px;line-height:1.22;text-shadow:0 1px 2px rgba(0,0,0,.3)}
.intro strong{font-size:20px;font-weight:500}
.story{left:251px;top:186px;width:265px;font-size:12.4px;line-height:1.03;color:var(--text)}
.story em{font-style:normal;color:var(--purple);font-weight:500;font-size:15.5px}
.section-title{color:var(--green);font-size:16px;font-weight:500}
.packages-title{left:19px;top:345px}
.packages{left:16px;top:370px;width:500px;border-collapse:separate;border-spacing:2px 0;font-size:11.5px}
.packages th{height:41px;color:#fff;font-size:15px;font-weight:500;line-height:1.02;text-align:center}
.packages th.col-service{background:var(--yellow);color:#222;text-align:left;padding-left:14px;width:184px}
.packages th.col-std{background:var(--olive)}
.packages th.col-enh{background:var(--green)}
.packages th.col-pre{background:var(--purple)}
.packages td{height:23px;text-align:center;border-bottom:2px solid #fff}
.packages td.svc{text-align:left;padding-left:14px;color:var(--grey);background:var(--row-a)}
.packages tr:nth-child(even) td.svc{background:#fafafa}
.packages td.std{background:var(--cell-std)}
.packages td.enh{background:var(--cell-enh)}
.packages td.pre{background:var(--cell-pre)}
.tick{color:var(--tick);font-size:16px}
.cross{color:var(--cross);font-size:14px}
.other-title{left:18px;top:612px}
.other-list{list-style:none;font-size:11.2px;font-weight:500;color:#333}
.other-list li{height:16.3px}
.other-list li::before{content:"✓ ";font-weight:400}
.other-list--a{left:16px;top:640px}
.other-list--b{left:132px;top:640px}
.contact--back{left:315px;top:639px;width:203px;height:83px;border:3px solid var(--green);border-radius:12px;padding-top:11px}
.contact--back .contact-lead{font-size:12px}
.contact--back .contact-phone{font-size:23px;margin:3px 0 1px}
.contact--back .contact-url{font-size:10.6px}
</style>
</head>
<body>

<section class="page page--front">
  <svg class="page-art" width="530" height="758" viewBox="0 0 530 758">
    <defs>
      <linearGradient id="lawnPhoto" x1="0" y1="0" x2="0" y2="1">
        <stop offset="0" stop-color="#3d9a35"/>
        <stop offset=".45" stop-color="#7fbf4e"/>
        <stop offset=".7" stop-color="#b9b8a8"/>
        <stop offset="1" stop-color="#5ea83a"/>
      </linearGradient>
      <linearGradient id="houseLawn" x1="0" y1="0" x2="0" y2="1">
        <stop offset="0" stop-color="#bfe0f4"/>
        <stop offset=".5" stop-color="#8a5a3e"/>
        <stop offset=".65" stop-color="#5fa63b"/>
        <stop offset="1" stop-color="#7cc34a"/>
      </linearGradient>
    </defs>
    <rect x="0" y="0" width="530" height="600" fill="url(#lawnPhoto)" role="img" aria-label="Photograph of a green lawn with a curving stone garden path"/>
    <path d="M0 0 H218 C240 90 320 140 420 170 C300 175 150 205 0 250 Z" fill="#fff"/>
    <path d="M0 235 C150 300 300 190 530 170 V205 C340 210 170 330 0 290 Z" fill="var(--purple)"/>
    <path d="M0 428 C80 398 170 378 240 393 C330 418 440 515 530 515 V758 H0 Z" fill="var(--green)"/>
    <path d="M0 438 C80 410 170 394 240 409 C330 438 440 548 530 553 V758 H0 Z" fill="var(--purple)"/>
    <path d="M0 452 C80 426 170 411 240 426 C330 458 440 568 530 578 V758 H0 Z" fill="#fff"/>
    <circle cx="300" cy="496" r="94" fill="url(#houseLawn)" stroke="#fff" stroke-width="8" role="img" aria-label="Photograph of a brick house behind a neatly striped lawn"/>
  </svg>

  <div class="abs brand"><span class="brand-mark"></span><span class="brand-name">Pelham Gardening Services</span></div>
  <p class="abs strapline">Lawn care by your local gardening expert</p>
  <div class="abs title-band"></div>
  <h1 class="abs service-title">Expert Lawn<br>Treatment Service</h1>

  <ul class="abs treatments">
    <li>Lawn Fertilising</li>
    <li>Scarification</li>
    <li>Aeration</li>
    <li>Weed Control</li>
    <li>Moss Control</li>
    <li>Hydration Booster</li>
    <li>Kempix</li>
    <li>Turfing &amp; Renovation</li>
  </ul>
  <p class="abs select-note">Select a one-off treatment or choose from one of our specially created lawn care packages.</p>

  <div class="abs contact contact--front">
    <p class="contact-lead">Call us for more information</p>
    <p class="contact-phone">01632 960481</p>
    <p class="contact-url">pelhamgardening.co.uk/lawncare</p>
  </div>
  <div class="abs grass-strip" role="img" aria-label="Strip of grass blades along the bottom edge"></div>
</section>

<section class="page page--back">
  <svg class="page-art" width="530" height="758" viewBox="0 0 530 758">
    <defs>
      <linearGradient id="grassTop" x1="0" y1="0" x2="1" y2="1">
        <stop offset="0" stop-color="#1f7a30"/>
        <stop offset="1" stop-color="#3fa23a"/>
      </linearGradient>
      <linearGradient id="stripedLawn" x1="0" y1="0" x2="1" y2="1">
        <stop offset="0" stop-color="#5aa93a"/>
        <stop offset=".6" stop-color="#7ccb47"/>
        <stop offset="1" stop-color="#9a9a90"/>
      </linearGradient>
    </defs>
    <path d="M0 0 H530 V130 C420 122 320 152 220 172 C140 188 60 172 0 150 Z" fill="url(#grassTop)" role="img" aria-label="Close-up photograph of lush grass"/>
    <path d="M200 180 C320 150 430 122 530 128 V152 C430 148 330 168 230 186 Z" fill="var(--purple)"/>
    <circle cx="126" cy="233" r="100" fill="url(#stripedLawn)" stroke="#fff" stroke-width="8" role="img" aria-label="Photograph of a striped lawn edged by a paved path"/>
  </svg>

  <p class="abs intro"><strong>As expert gardeners,</strong> we are passionate about horticulture and working to bring out the very best in your garden. When we work in your garden, we look at it and treat it with the same care and attention as if it were our own, before handing it back for you to enjoy. Our passion doesn't end at just trees and shrubs though. Your grass is as much of a living, breathing plant as your shrubs and we therefore utilise our expert horticultural knowledge to ensure your lawn thrives and reaches its fullest potential.</p>

  <p class="abs story">Lawn care isn't just about applying a fertiliser. It's about really understanding your lawn and being able to use <em>extensive knowledge and experience</em> to diagnose and treat issues. It therefore stands to reason that you should employ an expert to bring out the best in your lawn which is why we at Pelham Gardening Services have created a superior lawn care service that will keep your lawn looking lush, green and healthy all year round.</p>

  <h2 class="abs section-title packages-title">Lawn Treatment Packages</h2>
  <table class="abs packages">
    <thead>
      <tr><th class="col-service">Services</th><th class="col-std">Standard<br>Package</th><th class="col-enh">Enhanced<br>Package</th><th class="col-pre">Premium<br>Package</th></tr>
    </thead>
    <tbody>
      <tr><td class="svc">Spring Treatment</td><td class="std"><span class="tick">✓</span></td><td class="enh"><span class="tick">✓</span></td><td class="pre"><span class="tick">✓</span></td></tr>
      <tr><td class="svc">Early Summer Treatment</td><td class="std"><span class="tick">✓</span></td><td class="enh"><span class="tick">✓</span></td><td class="pre"><span class="tick">✓</span></td></tr>
      <tr><td class="svc">Late Summer Treatment</td><td class="std"><span class="tick">✓</span></td><td class="enh"><span class="tick">✓</span></td><td class="pre"><span class="tick">✓</span></td></tr>
      <tr><td class="svc">Autumn/Winter Treatment</td><td class="std"><span class="tick">✓</span></td><td class="enh"><span class="tick">✓</span></td><td class="pre"><span class="tick">✓</span></td></tr>
      <tr><td class="svc">Scarification</td><td class="std"><span class="cross">✕</span></td><td class="enh"><span class="tick">✓</span></td><td class="pre"><span class="tick">✓</span></td></tr>
      <tr><td class="svc">Aeration</td><td class="std"><span class="cross">✕</span></td><td class="enh"><span class="tick">✓</span></td><td class="pre"><span class="tick">✓</span></td></tr>
      <tr><td class="svc">Kempix Treatment</td><td class="std"><span class="cross">✕</span></td><td class="enh"><span class="cross">✕</span></td><td class="pre"><span class="tick">✓</span></td></tr>
      <tr><td class="svc">Hydration Boost Treatment</td><td class="std"><span class="cross">✕</span></td><td class="enh"><span class="cross">✕</span></td><td class="pre"><span class="tick">✓</span></td></tr>
    </tbody>
  </table>

  <h2 class="abs section-title other-title">Other Services offered</h2>
  <ul class="abs other-list other-list--a">
    <li>Lawn mowing</li><li>Shrub pruning</li><li>Hedge trimming</li><li>Weed killing</li><li>Planting &amp; design</li>
  </ul>
  <ul class="abs other-list other-list--b">
    <li>Garden clearance &amp; tidy-up</li><li>Regular Garden Maintenance</li><li>Turfing</li><li>Fencing</li><li>Gutter clearance</li>
  </ul>

  <div class="abs contact contact--back">
    <p class="contact-lead">Call us for more information</p>
    <p class="contact-phone">01632 960481</p>
    <p class="contact-url">pelhamgardening.co.uk/lawncare</p>
  </div>
  <div class="abs grass-strip" role="img" aria-label="Strip of grass blades along the bottom edge"></div>
</section>

</body>
</html>
```